Unique and original Business Card for Financial Services Business

I have moved premises and need to change the detail on my business card so thought now is a good time for a re-design. Looking for something professional and modern with colours to fit in with out logo. Like the idea of foil or embossing if that works but not a must have but I do want something that stands out and that I could not design myself.

Once business card is designed I will also be looking to get letterhead and flyers done but want the business card concept in place first.

The majority of designs I am receiving are generic and template based. I am looking for something unique and original. We have some great design elements in our logo, think outside the box and show me something that stands out from the crowd.

Target Market(s)

Business Professionals

Industry/Entity Type

Finance

Contact Information for Business Card

Name: Delia Norwood Phone 0473 958 162 Address PO Box 8617 Mossvale NSW 2389 Email info@steadyharbourfinancialservices.com.au website www.steadyharbourfinancialservices.com.au

Font styles to use
Other font styles liked:
• Ralway

Requirements
Should not have
• No black backgrounds please

```html
<!DOCTYPE html>
<html lang="en">
<head>
<meta charset="utf-8">
<title>Steady Harbour Financial Services – Business Card</title>
<link rel="stylesheet" href="https://fonts.googleapis.com/css2?family=Quicksand:wght@400;500&family=Raleway:wght@300&display=swap">
<style>
  :root {
    --teal: #0f7a80;
    --teal-dark: #0b6c72;
    --ink: #1d1d1f;
    --silver-light: #ececec;
    --silver-mid: #d6d6d6;
    --silver-dark: #c4c4c4;
    --emboss: #d3d3d3;
    --emboss-shadow: rgba(255,255,255,0.85);
    --emboss-edge: rgba(0,0,0,0.10);
    --page: #ffffff;
  }
  * { box-sizing: border-box; margin: 0; padding: 0; }
  html, body {
    width: 1200px; height: 1200px; overflow: hidden;
    background: var(--page);
  }
  .canvas { position: relative; width: 1200px; height: 1200px; }

  .card {
    position: absolute; left: 327px; width: 545px; height: 311px;
    background:
      linear-gradient(118deg, var(--silver-mid) 0%, var(--silver-light) 22%, var(--silver-mid) 40%, var(--silver-light) 58%, var(--silver-dark) 100%);
    overflow: hidden;
    font-family: "Quicksand", sans-serif;
  }
  .card--front { top: 240px; border-left: 8px solid var(--teal-dark); border-right: 8px solid var(--teal-dark); }
  .card--back  { top: 648px; border-top: 6px solid var(--teal-dark); border-bottom: 6px solid var(--teal-dark); }

  /* front */
  .brand { position: absolute; left: 0; right: 0; text-align: center; }
  .brand__mark {
    display: block; width: 50px; height: 50px; margin: 0 auto;
    background: var(--teal);
  }
  .brand__name {
    font-family: "Raleway", sans-serif; font-weight: 300;
    color: var(--teal); letter-spacing: 0.5px; white-space: nowrap;
  }
  .brand__tagline {
    font-family: "Raleway", sans-serif; font-weight: 300;
    color: #555; letter-spacing: 6px; white-space: nowrap;
  }
  .card--front .brand { top: 34px; }
  .card--front .brand__name { font-size: 25px; margin-top: 12px; line-height: 1.1; }
  .card--front .brand__tagline { font-size: 13px; line-height: 1.2; }

  .backdrop-shape {
    position: absolute; right: -40px; top: 100px; width: 260px; height: 260px;
    border-radius: 50%; background: rgba(200, 218, 224, 0.45);
  }

  .person { position: absolute; left: 22px; top: 212px; }
  .person__name { font-size: 21px; font-weight: 500; letter-spacing: 2px; color: var(--ink); line-height: 1.1; }
  .person__role { font-size: 14px; letter-spacing: 2.5px; color: var(--teal); line-height: 1.2; }

  .contact-front { position: absolute; right: 14px; top: 254px; text-align: right; font-size: 12.5px; color: var(--ink); line-height: 1.35; }
  .contact-front .phone-number { color: var(--teal); font-size: 14px; letter-spacing: 0.5px; }
  .contact-front .address { text-transform: uppercase; letter-spacing: 0.5px; }

  /* back */
  .card--back .brand { top: 52px; }
  .card--back .brand__mark {
    width: 90px; height: 90px; background: var(--emboss);
    box-shadow: 1px 1px 1px var(--emboss-shadow), -1px -1px 1px var(--emboss-edge);
  }
  .card--back .brand__name {
    font-size: 35px; color: var(--emboss); margin-top: 18px; line-height: 1.1;
    text-shadow: 1px 1px 0 var(--emboss-shadow), -1px -1px 0 var(--emboss-edge);
  }
  .card--back .brand__tagline {
    font-size: 18px; color: var(--emboss); letter-spacing: 11px; line-height: 1.3;
    text-shadow: 1px 1px 0 var(--emboss-shadow), -1px -1px 0 var(--emboss-edge);
  }
  .contact-back { position: absolute; left: 0; right: 0; top: 238px; text-align: center; }
  .contact-back__title { font-size: 15px; font-weight: 500; letter-spacing: 1px; color: var(--teal); line-height: 1.3; }
  .contact-back__line { font-size: 11.5px; color: var(--ink); line-height: 1.4; }
</style>
</head>
<body>
<div class="canvas">

  <section class="card card--front">
    <div class="backdrop-shape" role="img" aria-label="Faint brand emblem decoration"></div>
    <div class="brand">
      <span class="brand__mark"></span>
      <div class="brand__name">STEADY HARBOUR</div>
      <div class="brand__tagline">Financial Services</div>
    </div>
    <div class="person">
      <div class="person__name">DELIA NORWOOD</div>
      <div class="person__role">Business Finance</div>
    </div>
    <div class="contact-front">
      <div>Phone. <span class="phone-number">0473 958 162</span></div>
      <div class="address">PO Box 8617 Mossvale NSW 2389</div>
    </div>
  </section>

  <section class="card card--back">
    <div class="brand">
      <span class="brand__mark"></span>
      <div class="brand__name">STEADY HARBOUR</div>
      <div class="brand__tagline">Financial Services</div>
    </div>
    <div class="contact-back">
      <div class="contact-back__title">CONTACT ME</div>
      <div class="contact-back__line">www.steadyharbourfinancialservices.com.au</div>
      <div class="contact-back__line">info@steadyharbourfinancialservices.com.au</div>
    </div>
  </section>

</div>
</body>
</html>
```